Premium Lawn fertiliser packaging - Looking for long term designer

*Update at bottom
I need a carefully considered, bold and professional packaging design for my new premium lawn fertiliser product. This contest is for a detailed front of the stand-up pouch packaging and once I’ve chosen a winner, they’ll be asked to create the layout for the back that links to the front as well. I have a full range of additional products that will also need designs and so I'm looking for someone who can do a great job here and who we can work with long term.

The front should include our logo for Pemberly Turf Supply Direct and be titled “Bloom Vigor Max” "Professional Lawn Fertiliser". The spring fertiliser tag line is "Awaken your lawn: Lush Greening, Lasting Health".
Beneath it, it then needs to include some important usage information and the key benefits along with some suitable graphic.

Key information to include:

Apply March - June
Treats 35-50 m2
16-3-8
+2%MgO + 1% Fe + 2.9% CaO (this is the chemical makeup of the fertiliser and needs to be fairly prominent. If you look at other professional fertiliser packaging, you'll see how it needs to compare).

Key features:
Premium fertiliser, used by professionals
Advanced greening with micro-nutrient complex
Dual action Nitrogen: Instant green boost & continuous feed for 3 months
Child & pet safe

Our brand colours are purple and green. Purple = #592999, Green = 3cb64a / 81d742 / 4d9d44

I think these colours look great against a white background.

Please make sure you look at our website as well to get an idea of our brand: www.pemberlyturfsupply.co.uk

To help, I've attached images of competitors fertiliser packaging that I like the look of. I'm not looking for you to copy but just see what type of thing appeals to me, the standard I'm expecting and what I need to compete against....

In addition, I have also attached some potential images you may wish to try using in your design, although please feel free to use your own if you have something better. For the moment, the images are 'preview' images, but once I decide on a design and we agree on the correct image, I will download and send over a fully licensed version.

*** Update*** When submitting your design, can you submit it in 2 formats: The first as a fully printed custom stand-up pouch and the second as a full-size label stuck onto a standup pouch (whatever colour you think is right for your design - choose white if you are not sure). To explain, I've just discovered we won't be able to get full custom bags printed in time for the first run and so we will have to opt for the design to be printed on labels and fixed onto bags. I therefore need to choose a design that works in both formats as both a label on a standup pouch as well as a fully printed pouch. Many thanks.

Target Market(s)

Domestic home-owners

Industry/Entity Type

Lawn care. NOT AGRICULTURE OR FARMING

Font styles to use
Sans Serif

Requirements
Must have
• Presented in 2 formats - see update at bottom of description
Nice to have
• I quite like designs against a white background, although I’m open to other ideas as well.
Should not have
• Please do not include any people or faces in the design. The text should be solid in colour, so no graduated colour fill in the text or outline text. Please avoid over-busy or cluttered designs.

```html
<!DOCTYPE html>
<html lang="en">
<head>
<meta charset="utf-8">
<title>Bloom Vigor Max – Professional Lawn Fertiliser</title>
<link href="https://fonts.googleapis.com/css2?family=Archivo+Black&family=Open+Sans:ital,wght@0,400;0,600;1,600&family=Oswald:wght@400;500;600&display=swap" rel="stylesheet">
<style>
  :root{
    --purple:#592999;
    --purple-deep:#4a2288;
    --green:#3cb64a;
    --green-light:#81d742;
    --green-dark:#4d9d44;
    --brown:#3a2418;
    --ink:#2a1d16;
    --net:#1f3d24;
    --sky:#d4e9f7;
    --page:#f4f5f4;
    --white:#ffffff;
  }
  *{box-sizing:border-box;margin:0;padding:0}
  html,body{width:1200px;height:976px;overflow:hidden;background:var(--page)}
  .pouch-front{
    position:absolute;left:320px;top:8px;width:560px;height:960px;
    background:var(--white);overflow:hidden;
    box-shadow:0 2px 10px rgba(0,0,0,.08);
  }
  .sky{
    position:absolute;left:0;top:0;width:100%;height:470px;
    background:linear-gradient(180deg,#ffffff 0%,#f3f9fd 35%,var(--sky) 70%,#eef6fb 100%);
  }
  .brand{
    position:absolute;left:0;top:88px;width:100%;
    display:flex;align-items:center;justify-content:center;gap:12px;
  }
  .brand-dot{width:26px;height:26px;border-radius:50%;background:var(--green)}
  .brand-name{
    font-family:"Open Sans",sans-serif;font-weight:600;font-size:27px;
    color:var(--ink);letter-spacing:.3px;
  }
  .product-title{
    position:absolute;left:0;top:190px;width:100%;text-align:center;
    font-family:"Archivo Black",sans-serif;color:var(--purple);line-height:.95;
  }
  .product-title .line-1{display:block;font-size:96px;letter-spacing:1px}
  .product-title .line-2{display:block;font-size:64px;margin-top:4px}
  .category-pill{
    position:absolute;left:56px;top:370px;width:448px;height:40px;
    background:var(--green);border-radius:14px;
    display:flex;align-items:center;justify-content:center;
    font-family:"Open Sans",sans-serif;font-weight:400;font-size:21px;
    color:var(--white);letter-spacing:.6px;
  }
  .tagline{
    position:absolute;left:0;top:424px;width:100%;text-align:center;
    font-family:"Open Sans",sans-serif;font-style:italic;font-weight:600;
    font-size:17px;color:var(--ink);
  }
  .garden-photo{
    position:absolute;left:0;top:458px;width:100%;height:310px;
    background:linear-gradient(180deg,#eef6fb 0%,#dfe9e4 22%,#b9cfae 42%,#6f9a4a 60%,#5aa533 78%,#4f9a2c 100%);
  }
  .info-band{
    position:absolute;left:0;top:760px;width:100%;height:130px;
    background:var(--brown);
    border-top:4px solid var(--green-light);border-bottom:4px solid var(--green-light);
  }
  .features{
    position:absolute;top:30px;list-style:none;
    font-family:"Oswald",sans-serif;font-weight:400;font-size:11.5px;
    line-height:1.35;color:#e9e4de;
  }
  .features li{display:flex;gap:5px;margin-bottom:4px}
  .features svg{flex:none;margin-top:2px}
  .features-left{left:18px;width:118px}
  .features-right{left:420px;width:130px}
  .usage-badge{position:absolute;left:138px;top:-4px;width:284px;height:130px}
  .usage-badge svg{position:absolute;inset:0}
  .usage-text{
    position:absolute;inset:0;display:flex;flex-direction:column;
    align-items:center;justify-content:center;gap:4px;
    font-family:"Oswald",sans-serif;color:var(--white);text-align:center;
  }
  .usage-text .coverage,.usage-text .season{font-weight:500;font-size:21px;letter-spacing:.3px}
  .usage-text .formula{font-weight:400;font-size:15.5px}
  .net-weight{
    position:absolute;left:0;top:904px;width:100%;text-align:center;
    font-family:"Oswald",sans-serif;font-weight:500;font-size:26px;color:var(--net);
  }
</style>
</head>
<body>
  <main class="pouch-front">
    <div class="sky"></div>

    <div class="brand">
      <span class="brand-dot"></span>
      <span class="brand-name">Pemberly Turf Supply Direct</span>
    </div>

    <h1 class="product-title">
      <span class="line-1">BLOOM</span>
      <span class="line-2">VIGOR MAX</span>
    </h1>

    <div class="category-pill">PROFESSIONAL LAWN FERTILISER</div>
    <p class="tagline">Awaken your lawn: Lush Greening, Lasting Health</p>

    <div class="garden-photo" role="img" aria-label="Photograph of a bungalow with a white porch behind a lush green lawn, shrubs and conifers"></div>

    <section class="info-band">
      <ul class="features features-left">
        <li><svg width="9" height="9" viewBox="0 0 10 10"><path d="M1 5.5 4 8.5 9 1.5" fill="none" stroke="#81d742" stroke-width="2"/></svg><span>Premium fertiliser, used by professionals</span></li>
        <li><svg width="9" height="9" viewBox="0 0 10 10"><path d="M1 5.5 4 8.5 9 1.5" fill="none" stroke="#81d742" stroke-width="2"/></svg><span>Advanced greening with micro-nutrient complex</span></li>
      </ul>

      <div class="usage-badge">
        <svg viewBox="0 0 284 130" width="284" height="130">
          <polygon points="40,6 244,6 258,22 278,30 278,100 258,108 244,124 40,124 26,108 6,100 6,30 26,22" fill="#592999" stroke="#81d742" stroke-width="3"/>
          <polygon points="44,13 240,13 252,27 270,34 270,96 252,103 240,117 44,117 32,103 14,96 14,34 32,27" fill="none" stroke="#ffffff" stroke-width="1.2" opacity=".8"/>
        </svg>
        <div class="usage-text">
          <span class="coverage">TREATS 35-50 M2</span>
          <span class="formula">16-3-8 + 2%MgO + 1% Fe + 2.9% CaO</span>
          <span class="season">APPLY MARCH - JUNE</span>
        </div>
      </div>

      <ul class="features features-right">
        <li><svg width="9" height="9" viewBox="0 0 10 10"><path d="M1 5.5 4 8.5 9 1.5" fill="none" stroke="#81d742" stroke-width="2"/></svg><span>Dual action Nitrogen: Instant green boost &amp; continuous feed for 3 months</span></li>
        <li><svg width="9" height="9" viewBox="0 0 10 10"><path d="M1 5.5 4 8.5 9 1.5" fill="none" stroke="#81d742" stroke-width="2"/></svg><span>Child &amp; pet safe</span></li>
      </ul>
    </section>

    <p class="net-weight">NET WT. 25 LBS.</p>
  </main>
</body>
</html>
```